Yoga Teacher needs a Flyer for her Yin Yoga Teacher Training

I need a 4 x 6 postcard design for an in-person teacher training I'm offering in Doylestown, PA this summer. It needs to be full color both sides and I'll attach the printing and design specs below. My current logo is Nora Pelham logo in a pink script, which should be included somewhere. The biggest text should be "Yin Yoga Teacher Training" with the following smaller text somewhere on either the front or the back. August 4 - 8 at Bluewren Yoga Studio 287 Larch Avenue, Doylestown PA. For more details visit www.norapelhamyoga.example. And then if there's space on the back, please include this text: Discover the amazing benefits of yin yoga and somatic meditation in this 5-day in-person only immersion for both teachers and experienced students of yoga. Whether you’re interested in teaching or not, this weeklong course will deepen your yoga practice and change your life. You’ll learn 25 yin yoga postures and 5 somatic meditation techniques - all of which are incredible for pain relief and reducing tension. Not only will you be guided through the practice of these techniques, you’ll also participate in a vibrant discourse between teacher and student so you understand the why and the how behind what you’re learning. Nora Pelham has been leading yin yoga teacher trainings for the past 15 years and brings a wealth of information to the classroom. She’s also an expert at creating relaxed in-person learning environments where everyone feels safe to be themselves.
I've attached a bunch of different pictures that you can use. There should be one picture of me with my full body and one headshot. You can decide which picture goes on the front and which on the back - and feel free to crop or adjust any of the photos. I've also attached the color palette and font style guide for my brand. Reach out with any questions! Thank you!
Look and feel
Each slider illustrates characteristics of the customer's brand and the style your logo design should communicate.

```html
<!DOCTYPE html>
<html lang="en">
<head>
<meta charset="utf-8">
<title>Yin Yoga Teacher Training – Postcard</title>
<link href="https://fonts.googleapis.com/css2?family=Poppins:wght@300;400;500;600;800&display=swap" rel="stylesheet">
<style>
  :root {
    --page-bg: #e6e6e6;
    --ink: #111111;
    --pink: #e79cc0;
    --pink-soft: #f7c9d2;
    --pink-deep: #e25f9e;
    --teal: #457576;
    --teal-dot: #8fb9b9;
    --white: #ffffff;
  }
  * { box-sizing: border-box; margin: 0; padding: 0; }
  html, body { width: 1200px; height: 1080px; overflow: hidden; }
  body {
    background: var(--page-bg);
    font-family: "Poppins", sans-serif;
    position: relative;
  }
  .card {
    position: absolute;
    top: 173px;
    width: 493px;
    height: 729px;
    overflow: hidden;
  }
  /* Front */
  .card-front { left: 111px; background: var(--white); }
  .flower {
    position: absolute;
    border-radius: 50%;
    background: radial-gradient(circle at 40% 40%, #f6a9c9 0%, var(--pink-deep) 60%, rgba(226,95,158,0) 72%);
  }
  .flower-top { right: -40px; top: -60px; width: 200px; height: 160px; }
  .flower-bottom { left: -70px; bottom: -50px; width: 230px; height: 200px; }
  .brand-mark {
    position: absolute;
    left: 0; right: 0; top: 50px;
    text-align: center;
    color: var(--pink);
    font-weight: 300;
    font-size: 26px;
    letter-spacing: 1px;
    white-space: nowrap;
  }
  .title {
    position: absolute;
    left: 0; right: 0; top: 74px;
    text-align: center;
    font-weight: 800;
    font-size: 82px;
    line-height: 1;
    letter-spacing: -3px;
    color: var(--ink);
    white-space: nowrap;
  }
  .subtitle {
    position: absolute;
    left: 0; right: 0; top: 147px;
    text-align: center;
    font-weight: 400;
    font-size: 35px;
    color: var(--pink);
    white-space: nowrap;
  }
  .halo {
    position: absolute;
    left: 78px; top: 205px;
    width: 342px; height: 342px;
    border-radius: 50%;
    background: radial-gradient(circle, #f9d4d6 0%, var(--pink-soft) 70%, #f3b8c6 100%);
  }
  .portrait-full {
    position: absolute;
    left: 100px; top: 190px;
    width: 295px; height: 345px;
    border-radius: 140px 140px 60px 60px;
    background: linear-gradient(180deg, #3e2a22 0%, #1f8f95 35%, #1e2a36 65%, #ece3d6 100%);
    opacity: 0.9;
  }
  .details {
    position: absolute;
    left: 51px; top: 556px;
    width: 391px; height: 129px;
    border: 2px solid var(--ink);
    border-radius: 9px;
    overflow: hidden;
    background: var(--white);
  }
  .details-venue-mark {
    position: absolute;
    left: 0; top: 0;
    width: 126px; height: 92px;
    border-right: 2px solid var(--ink);
    display: flex; align-items: center; justify-content: center; gap: 6px;
    font-size: 15px; font-weight: 400; color: #4a3a45;
  }
  .details-venue-mark .dot { width: 10px; height: 10px; border-radius: 50%; background: #4a3a45; }
  .details-date {
    position: absolute;
    left: 126px; top: 0; right: 0; height: 38px;
    border-bottom: 2px solid var(--ink);
    padding-left: 12px;
    font-weight: 800; font-size: 29px; line-height: 38px;
    white-space: nowrap;
  }
  .details-address {
    position: absolute;
    left: 136px; top: 43px; right: 2px;
    font-size: 15.5px; line-height: 21px; font-weight: 400;
    white-space: nowrap;
  }
  .details-link {
    position: absolute;
    left: 0; right: 0; bottom: 0; height: 35px;
    background: var(--pink);
    color: var(--white);
    display: flex; align-items: center;
    padding-left: 8px; gap: 10px;
    white-space: nowrap;
  }
  .details-link .label { font-size: 13px; font-weight: 300; }
  .details-link .url { font-size: 15.5px; font-weight: 600; }
  /* Back */
  .card-back { left: 637px; background: var(--teal); color: var(--white); }
  .back-mark {
    position: absolute; left: 0; right: 0; top: 68px;
    text-align: center; font-size: 30px; font-weight: 300; letter-spacing: 1px;
  }
  .intro {
    position: absolute; left: 45px; right: 45px; top: 147px;
    text-align: center; font-size: 12.6px; line-height: 19.8px; font-weight: 300;
  }
  .intro p + p { margin-top: 19.8px; }
  .divider {
    position: absolute; left: 0; right: 0; top: 415px;
    display: flex; justify-content: center; gap: 9px;
  }
  .divider span { width: 6px; height: 6px; border-radius: 50%; background: var(--teal-dot); }
  .headshot {
    position: absolute; left: 56px; top: 464px;
    width: 156px; height: 206px;
    border: 3px solid var(--white);
    background: linear-gradient(160deg, #7f9a52 0%, #4d3a2e 40%, #1f8f95 70%, #f2b7c4 100%);
  }
  .about-title {
    position: absolute; left: 229px; top: 466px;
    font-size: 23px; font-weight: 500;
  }
  .about-text {
    position: absolute; left: 229px; top: 507px; width: 225px;
    font-size: 12.8px; line-height: 19.8px; font-weight: 300;
  }
</style>
</head>
<body>
  <section class="card card-front">
    <div class="flower flower-top" role="img" aria-label="Pink watercolour flower petals"></div>
    <div class="flower flower-bottom" role="img" aria-label="Pink watercolour flower petals"></div>
    <div class="brand-mark">Nora Pelham Yoga</div>
    <h1 class="title">YIN YOGA</h1>
    <div class="subtitle">Teacher Training</div>
    <div class="halo"></div>
    <div class="portrait-full" role="img" aria-label="Full-body photo of the teacher seated cross-legged in meditation"></div>
    <div class="details">
      <div class="details-venue-mark"><span class="dot"></span>Bluewren</div>
      <div class="details-date">AUGUST 4 - 8</div>
      <div class="details-address">Bluewren Yoga Studio, 287<br>Larch Avenue, Doylestown PA.</div>
      <div class="details-link"><span class="label">For more details</span><span class="url">www.norapelhamyoga.example</span></div>
    </div>
  </section>

  <section class="card card-back">
    <div class="back-mark">Nora Pelham Yoga</div>
    <div class="intro">
      <p>Discover the amazing benefits of yin yoga and somatic meditation in this 5-day in-person only immersion for both teachers and experienced students of yoga. Whether you’re interested in teaching or not, this weeklong course will deepen your yoga practice and change your life.</p>
      <p>You’ll learn 25 yin yoga postures and 5 somatic meditation techniques - all of which are incredible for pain relief and reducing tension. Not only will you be guided through the practice of these techniques, you’ll also participate in a vibrant discourse between teacher and student so you understand the why and the how behind what you’re learning.</p>
    </div>
    <div class="divider"><span></span><span></span><span></span><span></span></div>
    <div class="headshot" role="img" aria-label="Headshot of the teacher outdoors holding pink roses"></div>
    <h2 class="about-title">ABOUT ME</h2>
    <p class="about-text">Nora Pelham has been leading yin yoga teacher trainings for the past 15 years and brings a wealth of information to the classroom. She’s also an expert at creating relaxed in-person learning environments where everyone feels safe to be themselves.</p>
  </section>
</body>
</html>
```